Podcast artwork for a show focused on pharmaceutical medications!

Hi! We're in need of podcast artwork for a new podcast that will be launched in the next month or so. The show will be called "Underdosed" (see March 12th update below!) and will feature tons of different topics to inform the U.S. public about the public health issues of medications and how this is impacting society. The goal is for this show to educate, inform and then lead to action so that people can better protect themselves from harm and use medicines safely. The artwork will be the first impression to many people and we plan to heavily market the show. So we are taking this VERY seriously and have high expectations of a solid, clear, clean, memorable design. If you use images, please make sure you use high quality images! Final product will need to be delivered in multiple sizes (minimum 1400 X 1400 pixels needed and maximum 3000 X 3000, but artwork should look good in really small and really big sizes as it will appear in multiple ways in front of our audience; JPEG or PNG files). For examples of nice artwork/tips, check out this article from Hummleaf: https://www.hummleaf.example/blog/10-tips-create-awesome-podcast-artwork ; UPDATE March 10, 2018 - We have seen some good designs and in the last couple days of our contest here we wanted to send a message of encouragement to all designers who are interested in our project. Please don't hesitate to come up with your own ideas but stay away from basic clipart stuff! Figure out ways to make the show title clear and big enough to see in a small thumbnail size (again, think Tunevox and visit Tunevox to see how tiny the image becomes once you are at the episode view)! Also the word does not need to be spelled out as one long word (some designers have already figured that out). Lastly, don't shy away from using bold, crisp colors. UPDATE March 12, 2018 - Ok, we have seen some really nice designs and appreciate all the hard work but we decided to extend the deadline (yay!) to allow for even more designs (we want to get the most out of this campaign for the artwork we hope to stay with us forever!). That said, keep designing and keep submitting. Also, our team is throwing around the idea of calling the show "Nation of Tablets" (catchy, eh?). So feel free to design artwork around that title or "Underdosed". Whatever inspires you. Thank you!

Target Market(s)

Adults, age 18+

Industry/Entity Type

Media

Colors

Designer to choose colors to be used in the design.

Requirements
Must have
• Clear content, great colors, looks good both as a very small thumbnail as well a larger image.
Nice to have
• See link in project description for tips
Should not have

```html
<!DOCTYPE html>
<html lang="en">
<head>
<meta charset="utf-8">
<title>Underdosed — Podcast Artwork</title>
<link href="https://fonts.googleapis.com/css2?family=Alfa+Slab+One&display=swap" rel="stylesheet">
<style>
  :root {
    --band: #0d3d52;
    --band-deep: #082c3c;
    --page: #ffffff;
    --tile: #0a4058;
    --ink: #ffffff;
    --outline: #061e29;
    --capsule-a: #7fbf1e;
    --capsule-b: #f6c800;
    --capsule-c: #d0182c;
    --capsule-d: #0a85d0;
    --capsule-e: #e4470e;
  }
  * { margin: 0; padding: 0; box-sizing: border-box; }
  html, body { width: 1200px; height: 1000px; overflow: hidden; }
  body { position: relative; background: var(--page); }
  .band {
    position: absolute; left: 0; width: 1200px; height: 100px;
    background: linear-gradient(180deg, var(--band) 0%, var(--band-deep) 100%);
  }
  .band--top { top: 0; }
  .band--bottom { top: 900px; }
  .artwork {
    position: absolute; left: 225px; top: 125px;
    width: 750px; height: 750px; background: var(--tile);
  }
  .artwork svg { display: block; width: 750px; height: 750px; }
  .show-title {
    font-family: "Alfa Slab One", "Rockwell", serif;
    font-size: 212px;
    letter-spacing: -3px;
  }
  .show-title--outline {
    fill: var(--outline);
    stroke: var(--outline);
    stroke-width: 24px;
    stroke-linejoin: round;
  }
  .show-title--face { fill: var(--ink); }
</style>
</head>
<body>
  <div class="band band--top"></div>

  <main class="artwork">
    <svg viewBox="0 0 750 750" xmlns="http://www.w3.org/2000/svg">
      <defs>
        <linearGradient id="capsule-tones" x1="0" y1="0" x2="1" y2="1">
          <stop offset="0" stop-color="var(--capsule-a)"/>
          <stop offset="0.3" stop-color="var(--capsule-b)"/>
          <stop offset="0.5" stop-color="var(--capsule-c)"/>
          <stop offset="0.7" stop-color="var(--capsule-d)"/>
          <stop offset="1" stop-color="var(--capsule-e)"/>
        </linearGradient>
      </defs>

      <text class="show-title show-title--outline" aria-hidden="true">
        <tspan x="48" y="210">UN</tspan>
        <tspan x="48" y="370">DER</tspan>
        <tspan x="48" y="530">DO</tspan>
        <tspan x="48" y="690">SED</tspan>
      </text>
      <text class="show-title show-title--face" aria-label="Underdosed">
        <tspan x="48" y="210">UN</tspan>
        <tspan x="48" y="370">DER</tspan>
        <tspan x="48" y="530">DO</tspan>
        <tspan x="48" y="690">SED</tspan>
      </text>

      <rect class="capsule-cluster" role="img" aria-label="Cluster of colourful medicine capsules"
            x="525" y="400" width="190" height="295" rx="40" fill="url(#capsule-tones)" opacity="0.85"/>
    </svg>
  </main>

  <div class="band band--bottom"></div>
</body>
</html>
```